U.S. Popcorn company needs business cards

We are a popcorn company that manufactures popcorn and sells it to grocery stores worldwide. Our theme is "Americana" and our logo is U.S. route 66 which is the most famous highway in the U.S.

We would like the design to be simple and to use both sides. On the back side we would like to see just the logo and website. The front would be normal details

Target Market(s)

Wholesalers, grocers and distributors

Industry/Entity Type

Manufacture

Contact Information for Business Card

Business name: Bluebell Ridge Popcorn
Phone: +1 555 014 2286
Email: Derek@bluebellridgepopcorn.com
website: www.bluebellridgepopcorn.com
Tag Line: "POPular for a reason"
Name: Derek Halvorsen
Title: Founder/President

Requirements
Must have
• Either this design should be fun or clean and simple. I will let you show me your thougths.
Nice to have
• Anything that ties in the real Hwy Route 66.
• Colors might need to be red, white and blue incorporated.
Should not have
• Not be too busy.

```html
<!DOCTYPE html>
<html lang="en">
<head>
<meta charset="utf-8">
<title>Bluebell Ridge Popcorn – Business Cards</title>
<link rel="stylesheet" href="https://fonts.googleapis.com/css2?family=Open+Sans:wght@400;600;700&display=swap">
<style>
  :root {
    --page: #e9e6e0;
    --card-white: #f7f7f8;
    --navy: #25378f;
    --navy-deep: #1b2a78;
    --navy-light: #2f45a8;
    --red: #e0242e;
    --text-light: #ffffff;
  }
  html, body {
    margin: 0;
    padding: 0;
    width: 1200px;
    height: 780px;
    overflow: hidden;
    background: var(--page);
    font-family: "Open Sans", Arial, sans-serif;
  }
  .sheet {
    position: relative;
    width: 1200px;
    height: 780px;
  }
  .card {
    position: absolute;
    top: 230px;
    width: 560px;
    height: 320px;
    border-radius: 16px;
    overflow: hidden;
    box-shadow: 0 6px 18px rgba(0,0,0,0.18);
  }
  .card--front { left: 27px; background: var(--card-white); }
  .card--back {
    left: 613px;
    background: radial-gradient(ellipse at 50% 45%, var(--navy-light) 0%, var(--navy) 55%, var(--navy-deep) 100%);
  }
  .card__art { position: absolute; inset: 0; }

  .holder {
    position: absolute;
    top: 24px;
    right: 280px;
    text-align: right;
    white-space: nowrap;
  }
  .holder__name {
    margin: 0;
    color: var(--navy);
    font-size: 21px;
    font-weight: 400;
    line-height: 1.1;
  }
  .holder__title {
    margin: 3px 0 0;
    color: var(--red);
    font-size: 13px;
    font-weight: 400;
  }

  .brand {
    position: absolute;
    left: 34px;
    top: 150px;
    display: flex;
    align-items: center;
    gap: 10px;
    width: 200px;
  }
  .brand__dot {
    flex: none;
    width: 26px;
    height: 26px;
    border-radius: 50%;
    background: var(--red);
  }
  .brand__name {
    color: var(--navy);
    font-size: 21px;
    font-weight: 700;
    line-height: 1.15;
  }

  .contact {
    position: absolute;
    right: 18px;
    top: 78px;
    margin: 0;
    padding: 0;
    list-style: none;
    color: var(--text-light);
    font-size: 12.5px;
    line-height: 1;
    white-space: nowrap;
  }
  .contact__item {
    display: flex;
    align-items: center;
    justify-content: flex-end;
    gap: 8px;
    height: 24px;
  }
  .contact__icon {
    flex: none;
    width: 16px;
    height: 16px;
    border-radius: 3px;
    background: var(--red);
    display: flex;
    align-items: center;
    justify-content: center;
  }
  .contact__icon svg { width: 11px; height: 11px; fill: #fff; }

  .back__mark {
    position: absolute;
    left: 50%;
    top: 50%;
    width: 230px;
    height: 230px;
    margin: -115px 0 0 -115px;
    border-radius: 50%;
    background: rgba(255,255,255,0.06);
  }
  .back__text {
    position: absolute;
    inset: 0;
    display: flex;
    flex-direction: column;
    align-items: center;
    justify-content: center;
    color: var(--text-light);
  }
  .back__name {
    margin: 0;
    font-size: 31px;
    font-weight: 600;
    letter-spacing: 0.5px;
  }
  .back__web {
    margin: 10px 0 0;
    font-size: 15px;
    font-weight: 400;
  }
</style>
</head>
<body>
<main class="sheet">

  <section class="card card--front" aria-label="Business card front">
    <svg class="card__art" viewBox="0 0 560 320" aria-hidden="true">
      <path fill="var(--red)" d="M120 320 C190 302 235 265 252 212 C244 262 205 300 100 320 Z"/>
      <path fill="var(--navy)" d="M330 0 L560 0 L560 320 L170 320 C222 300 245 250 258 190 C272 120 290 50 330 0 Z"/>
      <path fill="var(--card-white)" d="M340 0 C300 50 282 120 268 190 C255 250 232 300 182 320 L205 320 C250 300 272 250 285 190 C300 120 320 50 360 0 Z"/>
    </svg>

    <div class="holder">
      <p class="holder__name">Derek Halvorsen</p>
      <p class="holder__title">Founder/President</p>
    </div>

    <div class="brand">
      <span class="brand__dot"></span>
      <span class="brand__name">Bluebell Ridge Popcorn</span>
    </div>

    <ul class="contact">
      <li class="contact__item">+1 555 014 2286
        <span class="contact__icon"><svg viewBox="0 0 24 24"><path d="M6.6 10.8a15.1 15.1 0 0 0 6.6 6.6l2.2-2.2c.3-.3.7-.4 1-.2 1.1.4 2.3.6 3.6.6.6 0 1 .4 1 1V20c0 .6-.4 1-1 1A17 17 0 0 1 3 4c0-.6.4-1 1-1h3.5c.6 0 1 .4 1 1 0 1.3.2 2.5.6 3.6.1.3 0 .7-.2 1z"/></svg></span>
      </li>
      <li class="contact__item">Derek@bluebellridgepopcorn.com
        <span class="contact__icon"><svg viewBox="0 0 24 24"><path d="M2 5h20v14H2zm2 2v.5l8 5 8-5V7l-8 5z"/></svg></span>
      </li>
      <li class="contact__item">www.bluebellridgepopcorn.com
        <span class="contact__icon"><svg viewBox="0 0 24 24"><path d="M12 2a10 10 0 1 0 0 20 10 10 0 0 0 0-20zm0 2c1 1.4 1.8 3.4 2 6h-4c.2-2.6 1-4.6 2-6zM4.1 13h3.9c.1 2.3.6 4.3 1.4 5.7A8 8 0 0 1 4.1 13zm0-2a8 8 0 0 1 5.3-5.7C8.6 6.7 8.1 8.7 8 11zm5.9 2h4c-.2 2.6-1 4.6-2 6-1-1.4-1.8-3.4-2-6zm4.6 5.7c.8-1.4 1.3-3.4 1.4-5.7h3.9a8 8 0 0 1-5.3 5.7zM16 11c-.1-2.3-.6-4.300-1.4-5.7A8 8 0 0 1 19.9 11z"/></svg></span>
      </li>
      <li class="contact__item">Millbrook, CA United States
        <span class="contact__icon"><svg viewBox="0 0 24 24"><path d="M12 2a7 7 0 0 0-7 7c0 5 7 13 7 13s7-8 7-13a7 7 0 0 0-7-7zm0 9.5A2.5 2.5 0 1 1 12 6.5a2.5 2.5 0 0 1 0 5z"/></svg></span>
      </li>
    </ul>
  </section>

  <section class="card card--back" aria-label="Business card back">
    <div class="back__mark"></div>
    <div class="back__text">
      <p class="back__name">BLUEBELL RIDGE POPCORN</p>
      <p class="back__web">www.bluebellridgepopcorn.com</p>
    </div>
  </section>

</main>
</body>
</html>
```